Homepage Redesign - Hi-tech business Law Firm

I'm looking for an updated graphic design (pdf file) for the homepage of dorvantlegal.ca (and which will form the general template of the other pages - but you don't need to design that). Detailed specs are in the Word file.

Deliverable is 1 pdf file that I find good looking, that sets forth the layout of the new page.

Target Market(s)

Sophisticated customers

Industry/Entity Type

Legal

Number of Pages Required

1 page

Requirements
Nice to have
• For a main background, tech type images to do with high powered boardrooms, computers, graphs, numbers, high tech manufacturing lines etc. Also, I tend to like blues and light greys, and uploaded a file today that shows my generally preferred layout, which a few of you have been getting close to.
Should not have
• Any mention of 'Personal Injury,' backgrounds that include books, or buildings with roman columns. Page should not be in dark colors or harsh on the eyes.

```html
<!DOCTYPE html>
<html lang="en">
<head>
<meta charset="utf-8">
<title>Dorvant Legal — Business Law</title>
<link href="https://fonts.googleapis.com/css2?family=Libre+Baskerville:wght@400;700&family=Poppins:wght@400;500;600;700&display=swap" rel="stylesheet">
<style>
:root{
  --navy:#073a5a;
  --navy-deep:#062f4a;
  --red:#d8262c;
  --gold:#f2b632;
  --mist:#e3eaef;
  --ink:#1d2530;
  --muted:#8a939c;
  --line:#e6e9ec;
  --white:#ffffff;
  --field:#f3f4f6;
}
*{box-sizing:border-box;margin:0;padding:0}
html,body{width:1200px;height:5111px;overflow:hidden}
body{position:relative;background:var(--white);font-family:"Poppins",sans-serif;color:var(--ink)}
.abs{position:absolute}
a{color:inherit;text-decoration:none}

/* top bar */
.topbar{left:595px;top:0;width:605px;height:24px;background:var(--navy);clip-path:polygon(14px 0,100% 0,100% 100%,0 100%);color:#dfe8ef;font:400 10px "Libre Baskerville",serif;display:flex;align-items:center;gap:26px;padding-left:40px}
.topbar span{display:flex;align-items:center;gap:5px;white-space:nowrap}
.topbar .mail{text-decoration:underline}
.topbar .call{margin-left:auto;margin-right:70px}

/* header */
.logo{display:flex;align-items:center;gap:10px}
.logo .mark{width:54px;height:54px;border:3px solid var(--navy)}
.logo .name{font:700 19px/1.15 "Libre Baskerville",serif;letter-spacing:4px;color:var(--navy)}
.header-logo{left:83px;top:22px}
.nav{top:56px;left:373px;font:400 12px "Libre Baskerville",serif;color:var(--navy)}
.nav a{position:absolute;white-space:nowrap}
.nav .active{text-decoration:underline}
.btn-outline{left:960px;top:44px;width:155px;height:40px;border:1px solid var(--navy);border-radius:3px;display:flex;align-items:center;justify-content:center;font:400 12px "Libre Baskerville",serif;color:var(--navy)}

/* hero */
.hero{left:0;top:100px;width:1200px;height:545px;background:linear-gradient(100deg,#3d5a6b 0%,#1f4960 40%,#0b3b57 70%,#0a3550 100%)}
.hero-portrait{left:730px;top:130px;width:330px;height:515px;background:linear-gradient(180deg,#7c8f9c 0%,#334a5c 45%,#1a2a3a 100%);border-radius:150px 150px 0 0;opacity:.55}
.hero-title{left:83px;top:222px;font:700 37px/50px "Libre Baskerville",serif;color:var(--white);white-space:nowrap}
.hero-text{left:83px;top:432px;font:400 12px/17px "Libre Baskerville",serif;color:#e7eef3}
.btn{display:flex;align-items:center;justify-content:center;gap:8px;font:700 14px "Libre Baskerville",serif;color:var(--white);border-radius:2px}
.btn-read{left:83px;top:500px;width:150px;height:38px;background:var(--navy)}
.btn-video{left:259px;top:500px;width:163px;height:38px;background:var(--red)}
.bar-gold{left:0;top:654px;width:381px;height:5px;background:var(--gold)}
.bar-navy{left:407px;top:654px;width:793px;height:5px;background:var(--navy)}

/* practices */
.practices{left:0;top:714px;width:1200px;height:929px;background:var(--mist)}
.section-title{font:700 28px "Libre Baskerville",serif;color:var(--navy)}
.btn-viewall{left:958px;top:768px;width:158px;height:40px;border:2px solid var(--navy);display:flex;align-items:center;justify-content:center;gap:8px;font:600 15px "Poppins",sans-serif;color:var(--navy);border-radius:2px}
.card{width:334px;height:318px;background:var(--white);border-radius:8px;box-shadow:0 4px 14px rgba(7,58,90,.06)}
.card .icon{position:absolute;left:40px;top:66px;width:34px;height:34px}
.card h3{position:absolute;left:40px;top:133px;font:400 18px "Libre Baskerville",serif;color:var(--ink);white-space:nowrap}
.card p{position:absolute;left:40px;top:175px;font:400 12px/18px "Libre Baskerville",serif;color:var(--muted)}
.card .more{position:absolute;left:40px;top:268px;font:500 15px "Poppins",sans-serif;color:#555;text-decoration:underline;text-underline-offset:4px}

/* case evaluation */
.form-card{left:83px;top:1682px;width:419px;height:530px;background:var(--white);border-radius:10px;box-shadow:0 4px 22px rgba(0,0,0,.09)}
.form-card h2{position:absolute;left:18px;top:38px;font:600 23px "Poppins",sans-serif;color:var(--navy)}
.form-card .sub{position:absolute;left:18px;top:82px;font:400 10px "Poppins",sans-serif;color:#a3a9af}
.field{position:absolute;background:var(--field);border-radius:4px;font:400 10px "Poppins",sans-serif;color:#a6acb2;padding:14px 10px}
.consent{position:absolute;left:18px;top:390px;width:330px;font:400 7.5px/12px "Poppins",sans-serif;color:#6b7278}
.consent b{color:var(--navy);font-weight:600}
.btn-send{position:absolute;left:125px;top:463px;width:171px;height:36px;background:var(--red);color:var(--white);font:500 15px "Poppins",sans-serif;display:flex;align-items:center;justify-content:center;border-radius:3px}
.about-title{left:591px;top:1776px}
.about-text{left:591px;top:1850px;width:520px;font:400 17px/36px "Libre Baskerville",serif;color:#5b6570}
.badge{background:var(--red);border-radius:6px}
.badge-about{left:591px;top:2093px;width:209px;height:56px}
.badge-note{left:814px;top:2099px;width:300px;font:400 9px/13px "Libre Baskerville",serif;color:#8a939c}

/* stats */
.stats{left:109px;top:2313px;width:982px;height:328px;background:var(--white);border-radius:10px;box-shadow:0 4px 22px rgba(0,0,0,.09);overflow:hidden}
.stat{position:absolute;top:0;width:245px;height:328px;text-align:center;border-right:1px solid var(--line)}
.stat svg{position:absolute;left:94px;top:72px}
.stat .num{position:absolute;left:0;right:0;top:172px;font:500 38px "Poppins",sans-serif;color:var(--ink)}
.stat .lbl{position:absolute;left:0;right:0;top:256px;font:400 15px "Poppins",sans-serif;color:#8b9196}
.stat-cta{position:absolute;left:736px;top:0;width:246px;height:328px;background:var(--navy);color:var(--white)}
.stat-cta h3{position:absolute;left:20px;top:64px;font:500 26px "Poppins",sans-serif}
.stat-cta p{position:absolute;left:20px;top:120px;width:215px;font:400 11px/18px "Poppins",sans-serif}
.btn-signup{position:absolute;left:20px;top:254px;width:141px;height:38px;background:var(--white);color:var(--navy);border-radius:20px;font:600 15px "Poppins",sans-serif;display:flex;align-items:center;justify-content:center}

/* testimonials */
.testimonials{left:0;top:2764px;width:1200px;height:553px;background:var(--mist)}
.center-title{left:0;width:1200px;text-align:center}
.quote-card{left:258px;top:2916px;width:682px;height:312px;background:var(--white)}
.quote-card .stars{position:absolute;left:0;right:0;top:46px;text-align:center}
.quote-card p{position:absolute;left:0;right:0;top:100px;text-align:center;font:400 16px/28px "Poppins",sans-serif;color:#6c7378}
.quote-card .who{position:absolute;left:0;right:0;top:244px;text-align:center;font:600 15px "Poppins",sans-serif;color:var(--ink)}
.quote-card .role{position:absolute;left:0;right:0;top:268px;text-align:center;font:400 9px "Poppins",sans-serif;color:#9aa0a6}
.arrow{width:34px;height:34px;border-radius:50%;display:flex;align-items:center;justify-content:center}
.arrow-prev{left:171px;top:3055px;background:var(--white)}
.arrow-next{left:992px;top:3055px;background:var(--navy)}

/* locations */
.loc{width:250px}
.loc h3{font:400 19px "Libre Baskerville",serif;color:var(--ink)}
.loc .addr{display:flex;gap:10px;margin-top:24px;font:400 10px/15px "Libre Baskerville",serif;color:#9aa0a6}
.loc .map{margin-top:20px;width:248px;height:244px;background:linear-gradient(135deg,#eef1ee 0%,#e4e9e6 50%,#dfe7ee 100%)}

/* news */
.news-big{left:171px;top:4073px;width:420px;height:411px;border-bottom:2px solid var(--navy);box-shadow:0 4px 14px rgba(0,0,0,.06)}
.news-big .img{height:220px;background:linear-gradient(160deg,#8aa6c4 0%,#4f6e92 45%,#2d3f56 100%)}
.date{font:600 9px "Poppins",sans-serif;color:var(--navy)}
.news-big .date{position:absolute;left:10px;top:238px}
.news-big h3{position:absolute;left:10px;top:262px;width:330px;font:400 16px/22px "Libre Baskerville",serif;color:#444}
.news-big p{position:absolute;left:10px;top:322px;width:330px;font:400 8px/12px "Libre Baskerville",serif;color:#8a939c}
.news-big .more{position:absolute;left:10px;top:382px;font:600 9px "Poppins",sans-serif;color:var(--navy);text-decoration:underline}
.news-small{left:607px;width:421px;height:123px;border-bottom:2px solid var(--navy);box-shadow:0 4px 14px rgba(0,0,0,.06)}
.news-small .img{position:absolute;left:0;top:0;width:159px;height:121px;background:linear-gradient(150deg,#d9d3cc 0%,#8b5a3c 55%,#4a2c1f 100%)}
.news-small h4{position:absolute;left:177px;top:30px;width:220px;font:400 12px/17px "Libre Baskerville",serif;color:#555}
.news-small .date{position:absolute;left:177px;top:98px}

/* footer */
.footer{left:0;top:4623px;width:1200px;height:488px;background:var(--navy-deep);color:var(--white)}
.footer .logo .mark{border-color:var(--white)}
.footer .logo .name{color:#c9d4dd}
.footer-text{font:400 12px/17px "Libre Baskerville",serif;color:#e6edf2}
.footer h4{font:700 18px "Libre Baskerville",serif;color:var(--white);white-space:nowrap}
.flinks{font:400 11px "Libre Baskerville",serif;color:#dfe7ee}
.flinks a{position:absolute;white-space:nowrap}
.contact-row{display:flex;gap:14px;font:400 11px/16px "Libre Baskerville",serif;color:#dfe7ee;white-space:nowrap}
.social{display:flex;gap:8px}
.social span{width:16px;height:16px;border-radius:50%;background:var(--white)}
.footer-bottom{font:400 11px "Poppins",sans-serif;color:#dfe7ee;white-space:nowrap}
</style>
</head>
<body>

<!-- top bar -->
<div class="abs topbar">
  <span><svg width="9" height="11" viewBox="0 0 10 12"><path d="M5 0a4 4 0 0 1 4 4c0 3-4 8-4 8S1 7 1 4a4 4 0 0 1 4-4z" fill="#fff"/></svg>GTA-Hamilton ·Niagara</span>
  <span class="mail"><svg width="11" height="8" viewBox="0 0 12 9"><rect x=".5" y=".5" width="11" height="8" fill="none" stroke="#fff"/><path d="M.5.5 6 5l5.5-4.5" fill="none" stroke="#fff"/></svg>contact@dorvantlegal.ca</span>
  <span class="call">Call Us <svg width="9" height="9" viewBox="0 0 10 10"><path d="M2 0l2 2-1 2c1 1 2 2 3 3l2-1 2 2-2 2C4 10 0 6 0 2z" fill="#fff"/></svg> 647 555 0142</span>
</div>

<!-- header -->
<div class="abs logo header-logo"><span class="mark"></span><span class="name">DORVANT<br>LEGAL</span></div>
<nav class="abs nav">
  <a class="active" style="left:0;top:0">Practice Areas ▾</a>
  <a style="left:127px;top:0">About</a>
  <a style="left:206px;top:0">News</a>
  <a style="left:282px;top:0">Resources</a>
  <a style="left:391px;top:0">Contact Us</a>
  <svg class="abs" style="left:498px;top:-2px" width="16" height="16" viewBox="0 0 16 16"><circle cx="6.5" cy="6.5" r="5" fill="none" stroke="#9aa3ab" stroke-width="1.5"/><path d="M10.5 10.5 15 15" stroke="#9aa3ab" stroke-width="1.5"/></svg>
  <svg class="abs" style="left:540px;top:-3px" width="30" height="18" viewBox="0 0 30 18"><circle cx="9" cy="5" r="4.5" fill="#073a5a"/><path d="M0 17c0-5 4-7 9-7s9 2 9 7z" fill="#073a5a"/><path d="M22 7l3 3 3-3z" fill="#073a5a"/></svg>
</nav>
<a class="abs btn-outline">Free Case Evaluation</a>

<!-- hero -->
<section class="abs hero" role="img" aria-label="Photo of a lawyer in a suit standing in front of a modern office backdrop"></section>
<div class="abs hero-portrait" role="img" aria-label="Portrait of the lead lawyer"></div>
<h1 class="abs hero-title">Winning.<br>My Client Depend On Me For It.<br>Why Shouldn’t You ?</h1>
<p class="abs hero-text">Lorem Ipsum is simply dummy text of the printing and typesetting industry.<br>Lorem Ipsum has been the industry's standard dummy text</p>
<a class="abs btn btn-read"><svg width="13" height="14" viewBox="0 0 13 14"><rect x="1" y="1" width="11" height="12" fill="none" stroke="#fff" stroke-width="1.5"/><path d="M4 1v12" stroke="#fff" stroke-width="1.5"/></svg>Read More</a>
<a class="abs btn btn-video"><svg width="14" height="10" viewBox="0 0 14 10"><rect x=".75" y=".75" width="12.5" height="8.5" rx="1.5" fill="none" stroke="#fff" stroke-width="1.5"/><path d="M5.5 3v4l3.5-2z" fill="#fff"/></svg>Video Library</a>
<div class="abs bar-gold"></div>
<div class="abs bar-navy"></div>

<!-- practices -->
<section class="abs practices"></section>
<h2 class="abs section-title" style="left:83px;top:768px">Area of Practices</h2>
<a class="abs btn-viewall">View All <svg width="28" height="10" viewBox="0 0 28 10"><path d="M0 5h26M22 1l4 4-4 4" fill="none" stroke="#073a5a" stroke-width="1.6"/></svg></a>

<div class="abs card" style="left:83px;top:853px">
  <svg class="icon" viewBox="0 0 34 34"><rect x="3" y="9" width="28" height="20" rx="2" fill="none" stroke="#073a5a" stroke-width="2.4"/><path d="M12 9V5h10v4M3 18h28M15 16h4v5h-4z" fill="none" stroke="#073a5a" stroke-width="2.4"/></svg>
  <h3>Business Litigation</h3>
  <p>Lorem Ipsum is simply dummy text<br>of the typesetting industry.</p>
  <a class="more">Learn More</a>
</div>
<div class="abs card" style="left:433px;top:853px">
  <svg class="icon" viewBox="0 0 34 34"><path d="M8 6l9 9M13 2l9 9M10 9l8-8M15 14l8-8M18 12l10 10M6 30h16" fill="none" stroke="#073a5a" stroke-width="2.4"/></svg>
  <h3>Professional Negligence</h3>
  <p>Lorem Ipsum is simply dummy text<br>of the typesetting industry.</p>
  <a class="more">Learn More</a>
</div>
<div class="abs card" style="left:783px;top:853px">
  <svg class="icon" viewBox="0 0 34 34"><path d="M7 12c0-7 5-10 10-10s10 3 10 10z" fill="none" stroke="#073a5a" stroke-width="2.4"/><rect x="5" y="12" width="24" height="4" fill="none" stroke="#073a5a" stroke-width="2.4"/><circle cx="17" cy="24" r="5" fill="none" stroke="#073a5a" stroke-width="2.4"/><path d="M5 32h24" stroke="#073a5a" stroke-width="2.4"/></svg>
  <h3>Fire Insurance</h3>
  <p>Lorem Ipsum is simply dummy text<br>of the typesetting industry.</p>
  <a class="more">Learn More</a>
</div>
<div class="abs card" style="left:83px;top:1240px">
  <svg class="icon" viewBox="0 0 34 34"><rect x="7" y="2" width="20" height="26" rx="2" fill="none" stroke="#073a5a" stroke-width="2.4"/><path d="M12 9h10M12 14h10M12 19h6M4 31h26" stroke="#073a5a" stroke-width="2.4"/></svg>
  <h3>Breach Of Contract</h3>
  <p>Lorem Ipsum is simply dummy text<br>of the typesetting industry.</p>
  <a class="more">Learn More</a>
</div>
<div class="abs card" style="left:433px;top:1240px">
  <svg class="icon" viewBox="0 0 34 34"><path d="M4 16 17 5l13 11M8 14v16h18V14" fill="none" stroke="#073a5a" stroke-width="2.4"/><path d="M13 22h8v8h-8z" fill="none" stroke="#073a5a" stroke-width="2.4"/></svg>
  <h3>real estate disputes</h3>
  <p>Lorem Ipsum is simply dummy text<br>of the typesetting industry.</p>
  <a class="more">Learn More</a>
</div>
<div class="abs card" style="left:783px;top:1240px">
  <svg class="icon" viewBox="0 0 34 34"><path d="M17 2 29 7v9c0 8-6 13-12 16C11 29 5 24 5 16V7z" fill="none" stroke="#073a5a" stroke-width="2.4"/><path d="m17 10 2 4h4l-3 3 1 4-4-2-4 2 1-4-3-3h4z" fill="#073a5a"/></svg>
  <h3>commercial arbitration</h3>
  <p>Lorem Ipsum is simply dummy text<br>of the typesetting industry.</p>
  <a class="more">Learn More</a>
</div>

<!-- case evaluation -->
<form class="abs form-card">
  <h2>CASE EVALUATION</h2>
  <p class="sub">Fill out this form to schedule your initial consult with our lawyers.</p>
  <div class="field" style="left:18px;top:123px;width:179px;height:48px">First Name*</div>
  <div class="field" style="left:211px;top:123px;width:178px;height:48px">Last Name*</div>
  <div class="field" style="left:18px;top:189px;width:179px;height:48px">Email*</div>
  <div class="field" style="left:211px;top:189px;width:178px;height:48px">Phone*</div>
  <div class="field" style="left:18px;top:262px;width:371px;height:111px">Case Details*</div>
  <p class="consent">*By using this site and or submitting this form, I agree to the <b>Privacy Policy</b><br>and <b>Terms of Use</b>.</p>
  <span class="btn-send">Send</span>
</form>
<h2 class="abs section-title about-title">Who We Are</h2>
<p class="abs about-text">Dorvant Legal is a boutique law office concentrating in Complex Business Litigation, Professional Negligence, Commercial Arbitration, and Insurance Coverage Disputes. Our innovative and pugnacious approach gets results for our clients in the Greater Toronto Area.</p>
<div class="abs badge badge-about" role="img" aria-label="Peer rating badge"></div>
<p class="abs badge-note">A top rating for a lawyer with strong experience. This rating shows the lawyer is highly respected by peers for high professional achievement and ethical standards.</p>

<!-- stats -->
<section class="abs stats">
  <div class="stat" style="left:0">
    <svg width="58" height="58" viewBox="0 0 58 58"><path d="M29 3l6 5 8-1 2 8 7 4-3 7 3 8-7 4-2 8-8-1-6 5-6-5-8 1-2-8-7-4 3-8-3-7 7-4 2-8 8 1z" fill="none" stroke="#2a8fc7" stroke-width="2"/><path d="m19 29 7 7 13-14" fill="none" stroke="#2a8fc7" stroke-width="2.5"/></svg>
    <div class="num">17+</div><div class="lbl">Years of Ligitation</div>
  </div>
  <div class="stat" style="left:245px">
    <svg width="58" height="58" viewBox="0 0 58 58"><path d="M29 3l6 5 8-1 2 8 7 4-3 7 3 8-7 4-2 8-8-1-6 5-6-5-8 1-2-8-7-4 3-8-3-7 7-4 2-8 8 1z" fill="none" stroke="#2a8fc7" stroke-width="2"/><path d="m19 29 7 7 13-14" fill="none" stroke="#2a8fc7" stroke-width="2.5"/></svg>
    <div class="num">900+</div><div class="lbl">Cases Won</div>
  </div>
  <div class="stat" style="left:490px">
    <svg width="58" height="58" viewBox="0 0 58 58"><path d="M29 3l6 5 8-1 2 8 7 4-3 7 3 8-7 4-2 8-8-1-6 5-6-5-8 1-2-8-7-4 3-8-3-7 7-4 2-8 8 1z" fill="none" stroke="#2a8fc7" stroke-width="2"/><path d="m19 29 7 7 13-14" fill="none" stroke="#2a8fc7" stroke-width="2.5"/></svg>
    <div class="num">840+</div><div class="lbl">Happy Clients</div>
  </div>
  <div class="stat-cta">
    <h3>Lorem Ipsum</h3>
    <p>Lorem Ipsum is simply dummy text of the typesetting industry.Lorem Ipsum is simply dummy text of the typesetting industry.</p>
    <span class="btn-signup">Sign Up</span>
  </div>
</section>

<!-- testimonials -->
<section class="abs testimonials"></section>
<h2 class="abs section-title center-title" style="top:2846px">What Our Client Saying</h2>
<div class="abs quote-card">
  <div class="stars"><svg width="164" height="26" viewBox="0 0 164 26"><g fill="#f2b632"><path id="st" d="m13 1 3.5 7.6 8.3.9-6.2 5.6 1.8 8.2L13 19.1l-7.4 4.2 1.8-8.2L1.2 9.5l8.3-.9z"/><use href="#st" x="34"/><use href="#st" x="68"/><use href="#st" x="102"/><use href="#st" x="136"/></g></svg></div>
  <p>Lorem Ipsum is simply dummy text<br>of the typesetting industry.Lorem<br>Ipsum is simply dummy text<br>of the typesetting industry.</p>
  <div class="who">John Smith</div>
  <div class="role">Manager</div>
</div>
<span class="abs arrow arrow-prev"><svg width="14" height="12" viewBox="0 0 14 12"><path d="M13 6H2M6 1 1 6l5 5" fill="none" stroke="#073a5a" stroke-width="1.6"/></svg></span>
<span class="abs arrow arrow-next"><svg width="14" height="12" viewBox="0 0 14 12"><path d="M1 6h11M8 1l5 5-5 5" fill="none" stroke="#fff" stroke-width="1.6"/></svg></span>

<!-- locations -->
<h2 class="abs section-title center-title" style="top:3382px">Locations</h2>
<div class="abs loc" style="left:171px;top:3495px">
  <h3>Hamilton</h3>
  <div class="addr"><svg width="12" height="16" viewBox="0 0 12 16"><path d="M6 0a6 6 0 0 1 6 6c0 4-6 10-6 10S0 10 0 6a6 6 0 0 1 6-6z" fill="#9aa0a6"/><circle cx="6" cy="6" r="2.2" fill="#fff"/></svg><span>12 Ashgrove Street, Ground<br>Floor Hamilton, ON L8N 2K4</span></div>
  <div class="map" role="img" aria-label="Street map around the Hamilton office"></div>
</div>
<div class="abs loc" style="left:478px;top:3495px">
  <h3>Niagara</h3>
  <div class="addr"><svg width="12" height="16" viewBox="0 0 12 16"><path d="M6 0a6 6 0 0 1 6 6c0 4-6 10-6 10S0 10 0 6a6 6 0 0 1 6-6z" fill="#9aa0a6"/><circle cx="6" cy="6" r="2.2" fill="#fff"/></svg><span>8 Orchard Lane Virgil,<br>ON L0S 1K2</span></div>
  <div class="map" role="img" aria-label="Street map around the Niagara office"></div>
</div>
<div class="abs loc" style="left:784px;top:3495px">
  <h3>Toronto</h3>
  <div class="addr"><svg width="12" height="16" viewBox="0 0 12 16"><path d="M6 0a6 6 0 0 1 6 6c0 4-6 10-6 10S0 10 0 6a6 6 0 0 1 6-6z" fill="#9aa0a6"/><circle cx="6" cy="6" r="2.2" fill="#fff"/></svg><span>220 Harbour Street Toronto,<br>ON M5J 2L6</span></div>
  <div class="map" role="img" aria-label="Street map around the Toronto office"></div>
</div>

<!-- news -->
<h2 class="abs section-title center-title" style="top:3982px">Latest News, Blogs</h2>
<article class="abs news-big">
  <div class="img" role="img" aria-label="Glass office towers seen from below against a cloudy sky"></div>
  <span class="date">Dec 12, 2023</span>
  <h3>Dorvant Legal joins Global Referral Network</h3>
  <p>Dorvant Legal is now a member of Meridian Global Referral Network — the largest legal referral network in the world — comprising 180 member firms located in more than 150 countries.</p>
  <a class="more">Read More</a>
</article>
<article class="abs news-small" style="top:4073px">
  <div class="img" role="img" aria-label="Wooden gavel resting on a desk"></div>
  <h4>Lorem ipsum dolor sit amet, consectetur adipiscing elit</h4>
  <span class="date">Dec 12, 2023</span>
</article>
<article class="abs news-small" style="top:4218px">
  <div class="img" role="img" aria-label="Wooden gavel resting on a desk"></div>
  <h4>Lorem ipsum dolor sit amet, consectetur adipiscing elit</h4>
  <span class="date">Dec 12, 2023</span>
</article>
<article class="abs news-small" style="top:4363px">
  <div class="img" role="img" aria-label="Wooden gavel resting on a desk"></div>
  <h4>Lorem ipsum dolor sit amet, consectetur adipiscing elit</h4>
  <span class="date">Dec 12, 2023</span>
</article>

<!-- footer -->
<footer class="abs footer">
  <div class="abs logo" style="left:83px;top:79px"><span class="mark"></span><span class="name">DORVANT<br>LEGAL</span></div>
  <p class="abs footer-text" style="left:83px;top:162px">Lorem Ipsum is simply dummy text<br>of the typesetting industry.</p>
  <h4 class="abs" style="left:83px;top:272px;font-size:15px">Follow Us On</h4>
  <div class="abs social" style="left:83px;top:299px" role="img" aria-label="Social media links"><span></span><span></span><span></span></div>

  <h4 class="abs" style="left:432px;top:58px">Quick Link</h4>
  <div class="abs flinks" style="left:432px;top:106px">
    <a style="top:0">Pratice Areas</a><a style="top:38px">About</a><a style="top:78px">News</a><a style="top:114px">Resources</a><a style="top:152px">Contact Us</a>
  </div>

  <h4 class="abs" style="left:607px;top:58px">Area of Practices</h4>
  <div class="abs flinks" style="left:607px;top:106px">
    <a style="top:0">Business Litigation</a><a style="top:40px">Professional Negligence</a><a style="top:80px">Commercial Arbitration</a>
  </div>
  <div class="abs badge" style="left:607px;top:261px;width:208px;height:46px" role="img" aria-label="Peer rating badge"></div>

  <h4 class="abs" style="left:873px;top:58px">Get In Touch</h4>
  <div class="abs contact-row" style="left:873px;top:106px"><svg width="12" height="16" viewBox="0 0 12 16"><path d="M6 0a6 6 0 0 1 6 6c0 4-6 10-6 10S0 10 0 6a6 6 0 0 1 6-6z" fill="#fff"/><circle cx="6" cy="6" r="2.2" fill="#062f4a"/></svg><span>12 Ashgrove Street E, Ground<br>Floor Hamilton, ON L8N 2K4</span></div>
  <div class="abs contact-row" style="left:873px;top:176px"><svg width="13" height="13" viewBox="0 0 10 10"><path d="M2 0l2 2-1 2c1 1 2 2 3 3l2-1 2 2-2 2C4 10 0 6 0 2z" fill="#fff"/></svg><span>+1 289-555-0178</span></div>
  <div class="abs contact-row" style="left:873px;top:211px"><svg width="13" height="10" viewBox="0 0 12 9"><rect x=".5" y=".5" width="11" height="8" fill="none" stroke="#fff"/><path d="M.5.5 6 5l5.5-4.5" fill="none" stroke="#fff"/></svg><span>hello@dorvantlegal.ca</span></div>

  <div class="abs footer-bottom" style="left:83px;top:430px">© 2023 Dorvant Legal. All Rights Reserved.</div>
  <div class="abs footer-bottom" style="left:813px;top:430px">Terms and Conditions</div>
  <div class="abs footer-bottom" style="left:960px;top:430px">Privacy Policy</div>
  <div class="abs footer-bottom" style="left:1053px;top:430px">Disclaimer</div>
</footer>

</body>
</html>
```